custom carpentry, woodworking and home repair company needs logo design and business card design

Attention: I apologize but I just received notification from my state that I cannot use the company name that I originally submitted (Beyond The Bench). The new name will be Joinolux We need a company logo and business card design for our new company based in the Hampton Roads area of Virginia. The company name is Joinolux. The final design should give a first impression of true craftsmanship and attention to detail. We would like the card to include the company name, my name Mark Tellman (owner), phone number (757) 348-2615, website (joinolux-example.com) and email address (mark@joinolux-example.com). Everything else is up to your discretion. Thanks, have fun, and good luck.

Industry/Entity Type

Business

Contact Information for Business Card

See project description

Logo Text

see project description

Colors

Designer to choose colors to be used in the design.

```html
<!DOCTYPE html>
<html lang="en">
<head>
<meta charset="utf-8">
<title>Joinolux Business Card</title>
<link rel="stylesheet" href="https://fonts.googleapis.com/css2?family=Arimo:wght@400;700&display=swap">
<style>
  :root {
    --page: #e9ecec;
    --card: #f4f4f4;
    --gold: #d5ae67;
    --grey: #97989c;
    --ink: #2a2a2a;
    --rule: #c9c9c9;
  }
  * { margin: 0; padding: 0; box-sizing: border-box; }
  html, body { width: 1200px; height: 1200px; overflow: hidden; }
  body {
    background: var(--page);
    font-family: "Arimo", Arial, sans-serif;
    display: flex;
    flex-direction: column;
    align-items: center;
    justify-content: center;
    gap: 56px;
  }
  .card {
    position: relative;
    width: 880px;
    height: 503px;
    background: var(--card);
    box-shadow: 0 6px 18px rgba(0,0,0,0.12);
    overflow: hidden;
  }
  .card-bands {
    position: absolute;
    inset: 0;
    width: 100%;
    height: 100%;
  }
  .band-gold { fill: var(--gold); }
  .band-grey { fill: var(--grey); }

  .wordmark {
    position: absolute;
    display: flex;
    align-items: center;
    gap: 14px;
    color: var(--gold);
    font-weight: 400;
    letter-spacing: 0.08em;
    text-transform: uppercase;
  }
  .wordmark-square {
    background: var(--gold);
    display: block;
  }
  .card--front .wordmark { left: 270px; top: 190px; font-size: 46px; }
  .card--front .wordmark-square { width: 34px; height: 34px; }
  .card--back .wordmark { left: 118px; top: 120px; font-size: 24px; }
  .card--back .wordmark-square { width: 18px; height: 18px; }

  .divider {
    position: absolute;
    left: 520px;
    top: 108px;
    width: 2px;
    height: 150px;
    background: var(--rule);
  }
  .contact {
    position: absolute;
    left: 566px;
    top: 100px;
  }
  .contact-name {
    font-size: 30px;
    font-weight: 700;
    color: var(--ink);
    margin-bottom: 22px;
    letter-spacing: 0.02em;
  }
  .contact-name .first { color: var(--gold); }
  .contact-list { list-style: none; }
  .contact-item {
    display: flex;
    align-items: center;
    gap: 16px;
    font-size: 20px;
    color: var(--ink);
    height: 34px;
  }
  .contact-icon { width: 22px; height: 22px; flex: none; }
  .contact-icon path, .contact-icon circle, .contact-icon rect { fill: var(--gold); }
  .contact-icon .cut { fill: none; stroke: var(--card); stroke-width: 1.6; }
</style>
</head>
<body>

  <section class="card card--back" aria-label="Business card, contact side">
    <svg class="card-bands" viewBox="0 0 880 503" preserveAspectRatio="none" aria-hidden="true">
      <polygon class="band-gold" points="0,300 300,300 282,330 0,330"/>
      <polygon class="band-grey" points="314,336 880,336 880,366 296,366"/>
    </svg>
    <div class="wordmark"><span class="wordmark-square"></span>Joinolux</div>
    <div class="divider"></div>
    <div class="contact">
      <p class="contact-name"><span class="first">Mark</span> Tellman</p>
      <ul class="contact-list">
        <li class="contact-item">
          <svg class="contact-icon" viewBox="0 0 24 24" aria-hidden="true"><path d="M6.6 10.8a15.1 15.1 0 0 0 6.6 6.6l2.2-2.2a1 1 0 0 1 1-.25 11.4 11.4 0 0 0 3.6.57 1 1 0 0 1 1 1V20a1 1 0 0 1-1 1A17 17 0 0 1 3 4a1 1 0 0 1 1-1h3.5a1 1 0 0 1 1 1c0 1.25.2 2.45.57 3.57a1 1 0 0 1-.25 1z"/></svg>
          (757) 348-2615
        </li>
        <li class="contact-item">
          <svg class="contact-icon" viewBox="0 0 24 24" aria-hidden="true"><rect x="2" y="5" width="20" height="14" rx="1"/><path class="cut" d="M2.5 5.5 12 13l9.5-7.5"/></svg>
          mark@joinolux-example.com
        </li>
        <li class="contact-item">
          <svg class="contact-icon" viewBox="0 0 24 24" aria-hidden="true"><circle cx="12" cy="12" r="10"/><path class="cut" d="M2 12h20M12 2c3 3 3 17 0 20M12 2c-3 3-3 17 0 20"/></svg>
          www.joinolux-example.com
        </li>
      </ul>
    </div>
  </section>

  <section class="card card--front" aria-label="Business card, logo side">
    <svg class="card-bands" viewBox="0 0 880 503" preserveAspectRatio="none" aria-hidden="true">
      <polygon class="band-gold" points="0,290 300,300 282,330 0,320"/>
      <polygon class="band-grey" points="314,336 880,370 880,400 296,366"/>
    </svg>
    <div class="wordmark"><span class="wordmark-square"></span>Joinolux</div>
  </section>

</body>
</html>
```